Wendlake Business Cards

Front and back. Martin Colfax MBA is the CEO of Wendlake Homes. Black white and grays. Logo and cool design.

Target Market(s)

Professional lenders and investors

Industry/Entity Type

Real estate developer. NO HOUSES OR ROOFS

Contact Information for Business Card

Logo, name and unique design. Front and back. Martin Colfax MBA is the CEO of Wendlake Homes. Black white and grays. Logo and cool design.

Font styles to use
Sans Serif

Colors

Designer to choose only greyscale colors for use in the design.

Requirements
Must have
• Cool look. Not the same card I could design.
Nice to have
• Something memorable
Should not have
• Basic

```html
<!DOCTYPE html>
<html lang="en">
<head>
<meta charset="utf-8">
<title>Wendlake Business Cards</title>
<link rel="stylesheet" href="https://fonts.googleapis.com/css2?family=Poppins:wght@300;400;600&display=swap">
<style>
  :root {
    --backdrop: #d8d9de;
    --card-black: #0a0a0a;
    --card-white: #f1f1f0;
    --ink: #1c1c1c;
    --ink-soft: #4a4a4a;
    --rule: #9a9a9a;
    --skyline-top: rgba(200, 200, 200, 0);
    --skyline-bottom: rgba(190, 190, 190, 0.55);
    --logo-white: #f4f4f4;
  }
  * { margin: 0; padding: 0; box-sizing: border-box; }
  html, body {
    width: 1200px; height: 800px; overflow: hidden;
    background: var(--backdrop);
    font-family: "Poppins", sans-serif;
  }
  .canvas {
    position: relative; width: 1200px; height: 800px;
    display: flex; align-items: center; justify-content: center; gap: 60px;
  }
  .card {
    position: relative; width: 520px; height: 300px;
    box-shadow: 0 10px 28px rgba(0, 0, 0, 0.18);
    overflow: hidden;
  }
  .card-front {
    background: var(--card-black);
    display: flex; align-items: center; justify-content: center;
  }
  .brand-name {
    color: var(--logo-white);
    font-weight: 600; font-size: 58px; letter-spacing: -1px;
  }
  .card-back { background: var(--card-white); color: var(--ink); }
  .skyline {
    position: absolute; left: 0; right: 0; bottom: 0; height: 190px;
    background: linear-gradient(180deg, var(--skyline-top), var(--skyline-bottom));
  }
  .identity { position: absolute; top: 46px; left: 0; right: 0; text-align: center; }
  .person-name { font-weight: 300; font-size: 28px; letter-spacing: 0.3px; }
  .person-title { font-weight: 300; font-size: 12px; color: var(--ink-soft); margin-top: 2px; }
  .contacts {
    position: absolute; top: 138px; left: 20px; right: 20px;
    display: flex; justify-content: space-between;
  }
  .contact {
    flex: 1; display: flex; flex-direction: column; align-items: center; gap: 10px;
    font-weight: 300; font-size: 12.5px;
  }
  .contact + .contact { border-left: 1px solid var(--rule); }
  .contact svg { width: 24px; height: 24px; fill: var(--ink); }
  .address {
    position: absolute; bottom: 34px; left: 0; right: 0; text-align: center;
    font-weight: 300; font-size: 12.5px; color: var(--ink-soft);
  }
</style>
</head>
<body>
<main class="canvas">
  <section class="card card-front">
    <span class="brand-name">Wendlake Homes</span>
  </section>

  <section class="card card-back">
    <div class="skyline" role="img" aria-label="Faint city skyline silhouette along the lower card edge"></div>
    <div class="identity">
      <h1 class="person-name">Martin Colfax MBA</h1>
      <p class="person-title">CEO of Wendlake Homes</p>
    </div>
    <div class="contacts">
      <div class="contact">
        <svg viewBox="0 0 24 24" aria-hidden="true"><path d="M2 5h20v14H2z M3 6l9 7 9-7" fill="none" stroke="#1c1c1c" stroke-width="0"/><path d="M2 5h20v1.5l-10 7.5L2 6.5z"/><path d="M2 8.5l10 7.5 10-7.5V19H2z"/></svg>
        <span>martin@wendlakehomes.com</span>
      </div>
      <div class="contact">
        <svg viewBox="0 0 24 24" aria-hidden="true"><rect x="2" y="6" width="5" height="15" rx="1.5"/><rect x="8" y="3" width="14" height="18" rx="1.5"/><rect x="10" y="5" width="10" height="4" fill="#f1f1f0"/><g fill="#f1f1f0"><rect x="10" y="11" width="2.5" height="2"/><rect x="13.8" y="11" width="2.5" height="2"/><rect x="17.5" y="11" width="2.5" height="2"/><rect x="10" y="15" width="2.5" height="2"/><rect x="13.8" y="15" width="2.5" height="2"/><rect x="17.5" y="15" width="2.5" height="2"/></g></svg>
        <span>1-555-014-2700</span>
      </div>
      <div class="contact">
        <svg viewBox="0 0 24 24" aria-hidden="true"><circle cx="12" cy="12" r="10"/><g fill="none" stroke="#f1f1f0" stroke-width="1.2"><ellipse cx="12" cy="12" rx="4.5" ry="10"/><path d="M2 12h20M4 7h16M4 17h16"/></g></svg>
        <span>www.wendlakehomes.com</span>
      </div>
    </div>
    <p class="address">418 Linden Ave, Houston, TX 77018, United States</p>
  </section>
</main>
</body>
</html>
```